Veltrix4 Business Card - Health

Veltrix4 maximizes value from the health data of its clients, including doctors, HMOs, and patients. I have attached the Veltrix4 logo as an ai and eps file.
Target Market(s)
Health, HMO, Healthcare, Data, Big Data, Data Analytics
Industry/Entity Type
Business
Requirements
Must have
- At least one side should have some white on it so that we can write on it.

```html
<!DOCTYPE html>
<html lang="en">
<head>
<meta charset="utf-8">
<title>Veltrix4 Business Card</title>
<link rel="stylesheet" href="https://fonts.googleapis.com/css2?family=Questrial&family=Open+Sans:wght@400&display=swap">
<style>
  :root {
    --canvas: #dde3e2;
    --card: #ffffff;
    --ink: #1d2124;
    --muted: #7b898d;
    --blue: #2a7cf6;
    --cyan: #5eeefc;
    --pattern-a: rgba(120, 170, 235, 0.38);
    --pattern-b: rgba(190, 215, 245, 0.18);
  }
  * { margin: 0; padding: 0; box-sizing: border-box; }
  html, body { width: 1011px; height: 1200px; overflow: hidden; }
  body { background: var(--canvas); position: relative; font-family: "Open Sans", sans-serif; }

  .card { position: absolute; background: var(--card); overflow: hidden; }
  .card--front { left: 33px; top: 10px; width: 948px; height: 571px; }
  .card--back { left: 30px; top: 618px; width: 948px; height: 568px; }

  .pattern { position: absolute; }
  .card--front .pattern {
    right: 0; top: 0; width: 620px; height: 571px;
    background: radial-gradient(ellipse at 85% 15%, var(--pattern-a), var(--pattern-b) 55%, rgba(255,255,255,0) 80%);
  }
  .card--back .pattern {
    right: 0; bottom: 0; width: 948px; height: 420px;
    background: radial-gradient(ellipse at 75% 80%, var(--pattern-a), var(--pattern-b) 50%, rgba(255,255,255,0) 78%);
  }

  .brand { position: absolute; display: flex; align-items: center; }
  .brand__dot { border-radius: 50%; background: var(--blue); flex: none; }
  .brand__name { font-family: "Questrial", sans-serif; color: var(--ink); font-weight: 400; line-height: 1; letter-spacing: -1px; }
  .card--front .brand { left: 133px; top: 144px; }
  .card--front .brand__dot { width: 100px; height: 100px; margin-right: 47px; }
  .card--front .brand__name { font-size: 92px; }
  .card--back .brand { left: 227px; top: 168px; }
  .card--back .brand__dot { width: 108px; height: 108px; margin-right: 47px; }
  .card--back .brand__name { font-size: 99px; }

  .contacts { position: absolute; left: 78px; top: 334px; list-style: none; }
  .contacts li { display: flex; align-items: center; height: 43.5px; font-size: 21.5px; color: var(--muted); }
  .contacts svg { width: 44px; height: 32px; margin-right: 36px; fill: var(--blue); flex: none; }

  .band { position: absolute; left: 0; top: 437px; width: 948px; height: 71px; }
  .band svg.band__shape { position: absolute; inset: 0; }
  .services { position: absolute; left: 0; top: 0; height: 71px; width: 100%; list-style: none; }
  .services li { position: absolute; top: 0; height: 71px; display: flex; align-items: center; font-size: 23px; color: var(--ink); }
  .services svg { width: 56px; height: 56px; margin-right: 6px; }
  .services .svc-big { left: 78px; }
  .services .svc-analytics { left: 242px; }
  .services .svc-health { left: 470px; }
</style>
</head>
<body>

<section class="card card--front">
  <div class="pattern" role="img" aria-label="Soft overlapping pale blue diamond pattern"></div>
  <div class="brand">
    <span class="brand__dot"></span>
    <span class="brand__name">Veltrix4</span>
  </div>
  <ul class="contacts">
    <li>
      <svg viewBox="0 0 44 32"><path d="M14 4c2-1 3 0 4 2l2 4c1 2 0 3-1 4l-2 2c1 3 4 6 7 7l2-2c1-1 2-2 4-1l4 2c2 1 3 2 2 4l-1 3c-1 2-3 3-6 2C19 29 11 21 9 11c-1-3 0-5 2-6z"/></svg>
      +84 061 482 715
    </li>
    <li>
      <svg viewBox="0 0 44 32"><rect x="2" y="4" width="40" height="26" rx="1"/><path d="M4 6l18 14L40 6" stroke="#fff" stroke-width="2.4" fill="none"/><path d="M4 28l13-11M40 28L27 17" stroke="#fff" stroke-width="2" fill="none"/></svg>
      hello@veltrix4.net
    </li>
    <li>
      <svg viewBox="0 0 44 32"><path d="M22 1a10 10 0 0 0-10 10c0 8 10 20 10 20s10-12 10-20A10 10 0 0 0 22 1zm0 14a4 4 0 1 1 0-8 4 4 0 0 1 0 8z"/></svg>
      PO, BOX 218 Norvale
    </li>
    <li>
      <svg viewBox="0 0 44 32"><g fill="none" stroke="#2a7cf6" stroke-width="3.4" stroke-linecap="round"><path d="M6 12a23 23 0 0 1 32 0"/><path d="M12 18a14 14 0 0 1 20 0"/></g><circle cx="22" cy="25" r="3.5"/></svg>
      www.veltrix4.net
    </li>
  </ul>
</section>

<section class="card card--back">
  <div class="pattern" role="img" aria-label="Soft overlapping pale blue diamond pattern"></div>
  <div class="brand">
    <span class="brand__dot"></span>
    <span class="brand__name">Veltrix4</span>
  </div>
  <div class="band">
    <svg class="band__shape" viewBox="0 0 948 71" preserveAspectRatio="none">
      <polygon points="0,0 701,0 758,71 0,71" fill="var(--cyan)"/>
      <polygon points="711,0 948,0 948,71 768,71" fill="var(--blue)"/>
    </svg>
    <ul class="services">
      <li class="svc-big">
        <svg viewBox="0 0 56 56"><path d="M14 40l-8 10" stroke="#e9f7fb" stroke-width="6" stroke-linecap="round"/><circle cx="31" cy="25" r="20" fill="#fff" stroke="#2a7cf6" stroke-width="2.5"/><g fill="none" stroke="#2a7cf6" stroke-width="2"><rect x="22" y="14" width="18" height="6"/><rect x="22" y="22" width="18" height="6"/><rect x="22" y="30" width="18" height="6"/></g></svg>
        Big Data
      </li>
      <li class="svc-analytics">
        <svg viewBox="0 0 56 56"><path d="M14 40l-8 10" stroke="#e9f7fb" stroke-width="6" stroke-linecap="round"/><circle cx="31" cy="25" r="20" fill="#fff" stroke="#2a7cf6" stroke-width="2.5"/><g fill="#2a7cf6"><rect x="22" y="26" width="3" height="9"/><rect x="27" y="20" width="3" height="15"/><rect x="32" y="23" width="3" height="12"/><rect x="37" y="17" width="3" height="18"/></g></svg>
        Data Analytics
      </li>
      <li class="svc-health">
        <svg viewBox="0 0 56 56"><path d="M14 40l-8 10" stroke="#e9f7fb" stroke-width="6" stroke-linecap="round"/><circle cx="31" cy="25" r="20" fill="#fff" stroke="#2a7cf6" stroke-width="2.5"/><rect x="21" y="17" width="20" height="16" rx="2" fill="#ffd36b"/><path d="M31 20v10M26 25h10" stroke="#f0552e" stroke-width="3"/></svg>
        Health
      </li>
    </ul>
  </div>
</section>

</body>
</html>
```